Bram's limocello

Hello Artfolkly, we need a label design for Bram’s Limoncello our first product of our new distillery. We want some simple, clean, bold graphics with a contemporary look. With only three or four colors so it can be printed on a label about three and a half inches square. We admire the art of Anton Verhulst specifically his intense colors, high contrast and whimsical humor.
We are located in Eagle Colorado which is near the ski resorts of Tusk and Granite Hollow. Our target consumer is sophisticated and affluent. Limoncello is a sweet Italian lemon liqueur which is gaining popularity in American cities. We don’t have any preconceived ideas so are open to any and all design concepts.

Cheers! 514 Distillery LLC

```html
<!DOCTYPE html>
<html lang="en">
<head>
<meta charset="utf-8">
<title>Bram’s Limoncello – Label</title>
<link rel="stylesheet" href="https://fonts.googleapis.com/css2?family=Josefin+Sans:wght@100;200&display=swap">
<style>
  :root {
    --page: #ffffff;
    --label: #231f20;
    --lemon: #fbe200;
    --lemon-line: #f5e82a;
    --ink-light: #f2f2f2;
  }
  html, body {
    margin: 0;
    width: 1200px;
    height: 1000px;
    overflow: hidden;
    background: var(--page);
  }
  .canvas {
    position: relative;
    width: 1200px;
    height: 1000px;
  }
  .label {
    position: absolute;
    left: 255px;
    top: 154px;
    width: 690px;
    height: 690px;
    overflow: hidden;
    background: var(--label);
    font-family: "Josefin Sans", sans-serif;
    font-weight: 200;
    text-transform: uppercase;
  }
  .label__maker {
    position: absolute;
    left: 106px;
    top: 33px;
    margin: 0;
    font-size: 30px;
    line-height: 1;
    color: var(--ink-light);
    letter-spacing: -1px;
  }
  .label__name {
    position: absolute;
    left: 64px;
    top: 76px;
    margin: 0;
    font-size: 100px;
    font-weight: 200;
    line-height: 1;
    color: var(--lemon-line);
    letter-spacing: -10px;
    white-space: nowrap;
  }
  .label__kind {
    position: absolute;
    right: 52px;
    top: 170px;
    margin: 0;
    font-size: 34px;
    line-height: 1;
    color: var(--ink-light);
    letter-spacing: -1px;
    white-space: nowrap;
  }
  .label__splash {
    position: absolute;
    left: 28px;
    top: 230px;
    width: 540px;
    height: 400px;
    background:
      radial-gradient(ellipse 120px 150px at 130px 200px, var(--lemon) 0%, rgba(251,226,0,0.55) 45%, rgba(251,226,0,0) 100%),
      radial-gradient(circle 45px at 362px 322px, rgba(251,226,0,0.7) 0%, rgba(251,226,0,0) 100%),
      radial-gradient(circle 30px at 512px 42px, rgba(251,226,0,0.7) 0%, rgba(251,226,0,0) 100%);
  }
  .label__volume,
  .label__strength {
    position: absolute;
    bottom: 26px;
    margin: 0;
    font-size: 28px;
    line-height: 1;
    color: var(--ink-light);
    letter-spacing: -1px;
    white-space: nowrap;
  }
  .label__volume { left: 22px; }
  .label__strength { right: 24px; }
</style>
</head>
<body>
  <main class="canvas">
    <section class="label">
      <p class="label__maker">Bram’s</p>
      <h1 class="label__name">Limoncello</h1>
      <p class="label__kind">Lemon Liqueur</p>
      <div class="label__splash" role="img" aria-label="Yellow paint splatter with scattered lemon-coloured drops"></div>
      <p class="label__volume">750ml</p>
      <p class="label__strength">30% Acl/Vol (60 Proof)</p>
    </section>
  </main>
</body>
</html>
```